Landing promo page for a Travel/Lifestyle app

Landing promotion page is needed for a new travel/Lifestyle app in English. We would like to have the logo of the company... and a brief info about our app, and two links to take you to Vendra Hub store or Nimbo Shelf to download the app. One or several application screens can be shown.

Target Market(s)

Travel, leisure, holidays

Industry/Entity Type

Travel

Font styles to use
Sans Serif

Requirements
Must have
• logo, colors of the logo
• 2 buttons for vendra hub and tevo shelf
• screen shots of the app screen
• a brief introduction to the app (about 100 words) I'll post this later
• modern, fresh, minimalist, contemporary, clean,
Nice to have
• abstract design,
Should not have
• different colors of the logo or pictures of people or animals.

```html
<!DOCTYPE html>
<html lang="en">
<head>
<meta charset="utf-8">
<title>Summit Roamer — Travel App</title>
<link href="https://fonts.googleapis.com/css2?family=Comfortaa:wght@400;700&family=Poppins:wght@400;500&family=Lora:ital@0;1&display=swap" rel="stylesheet">
<style>
  :root {
    --purple: #5b4e96;
    --teal: #52a9a0;
    --teal-light: #4fc3b8;
    --white: #ffffff;
    --sky: #ece8e1;
    --gold: #c9a468;
    --earth: #7d5a2f;
  }
  * { margin: 0; padding: 0; box-sizing: border-box; }
  html, body { width: 1200px; height: 711px; overflow: hidden; background: var(--white); }
  .page { position: relative; width: 1200px; height: 711px; overflow: hidden; }
  .hero-photo {
    position: absolute; inset: 0 0 100px 0;
    background:
      radial-gradient(circle at 92% 38%, rgba(255,250,235,0.95) 0, rgba(255,240,210,0.4) 10%, transparent 24%),
      linear-gradient(180deg, #dfe3e6 0%, var(--sky) 22%, #e6d8c2 36%, var(--gold) 50%, #a7793f 68%, var(--earth) 100%);
  }
  .wave { position: absolute; inset: 0; width: 1200px; height: 711px; }
  .brand {
    position: absolute; top: 38px; left: 0; width: 1200px;
    display: flex; flex-direction: column; align-items: center; gap: 12px;
  }
  .brand-dot { width: 44px; height: 44px; border-radius: 50%; background: var(--teal); }
  .brand-name {
    font-family: "Comfortaa", sans-serif; font-weight: 700; font-size: 16px;
    letter-spacing: 3px; color: var(--purple);
  }
  .headline {
    position: absolute; left: 218px; top: 262px;
    font-family: "Comfortaa", sans-serif; color: var(--white); font-weight: 400;
  }
  .headline .lead { display: block; font-size: 37px; line-height: 38px; }
  .headline .accent { display: block; font-size: 54px; line-height: 62px; letter-spacing: -0.5px; }
  .actions { position: absolute; left: 225px; top: 442px; display: flex; gap: 14px; }
  .btn {
    width: 135px; height: 42px; border-radius: 21px; border: none;
    font-family: "Poppins", sans-serif; font-size: 12.5px; color: var(--white);
    display: flex; align-items: center; justify-content: center; letter-spacing: 0.3px;
  }
  .btn-primary { background: var(--purple); }
  .btn-secondary { background: var(--teal); }
  .screen {
    position: absolute; border-radius: 6px; overflow: hidden;
    background: linear-gradient(180deg, var(--teal-light) 0%, #4b9fb0 45%, var(--purple) 100%);
    box-shadow: 0 10px 24px rgba(0,0,0,0.25);
    color: var(--white); font-family: "Lora", serif; text-align: center;
  }
  .screen-back { left: 800px; top: 282px; width: 112px; height: 280px; }
  .screen-front { left: 735px; top: 317px; width: 112px; height: 258px; }
  .status { display: flex; justify-content: space-between; padding: 4px 6px; font-family: "Poppins", sans-serif; font-size: 5px; }
  .app-mark { margin: 20px auto 4px; width: 14px; height: 14px; border-radius: 50%; background: var(--white); }
  .app-name { font-family: "Comfortaa", sans-serif; font-size: 3.5px; letter-spacing: 0.8px; }
  .quote { margin: 36px 8px 0; font-size: 7.2px; line-height: 10.5px; }
  .author { margin-top: 14px; font-size: 5px; font-style: italic; }
  .hop-btn {
    margin: 40px auto 0; width: 72px; height: 14px; border-radius: 7px;
    background: var(--white); color: var(--purple);
    font-family: "Poppins", sans-serif; font-size: 6px; line-height: 14px;
  }
</style>
</head>
<body>
<main class="page">
  <div class="hero-photo" role="img" aria-label="Traveller standing in golden grass on a hillside above the sea at sunset"></div>

  <svg class="wave" viewBox="0 0 1200 711" aria-hidden="true">
    <path fill="#ffffff" d="M-4,588 c25,-28 35,-40 56,-40 c21,0 31,12 56,40 c25,-28 35,-40 56,-40 c21,0 31,12 56,40 c25,-28 35,-40 56,-40 c21,0 31,12 56,40 c25,-28 35,-40 56,-40 c21,0 31,12 56,40 c25,-28 35,-40 56,-40 c21,0 31,12 56,40 c25,-28 35,-40 56,-40 c21,0 31,12 56,40 c25,-28 35,-40 56,-40 c21,0 31,12 56,40 c25,-28 35,-40 56,-40 c21,0 31,12 56,40 c25,-28 35,-40 56,-40 c21,0 31,12 56,40 c25,-28 35,-40 56,-40 c21,0 31,12 56,40 c25,-28 35,-40 56,-40 c21,0 31,12 56,40 L1228,711 L-4,711 Z"/>
  </svg>

  <header class="brand">
    <span class="brand-dot"></span>
    <span class="brand-name">SUMMIT ROAMER</span>
  </header>

  <h1 class="headline">
    <span class="lead">Summit Roamer makes</span>
    <span class="lead">your life more</span>
    <span class="accent">COMFORTABLE</span>
  </h1>

  <nav class="actions">
    <a class="btn btn-primary">GET STARTED</a>
    <a class="btn btn-secondary">READ MORE</a>
  </nav>

  <section class="screen screen-back" aria-label="App welcome screen">
    <div class="status"><span>9:41</span><span>●●●</span></div>
    <div class="app-mark"></div>
    <div class="app-name">SUMMIT ROAMER</div>
    <p class="quote">“Traveling - it leaves you speechless, then turns you into a storyteller”</p>
    <p class="author">- Mira Castell</p>
    <div class="hop-btn">Let's Hop</div>
  </section>

  <section class="screen screen-front" aria-label="App welcome screen">
    <div class="status"><span>9:41</span><span>●●●</span></div>
    <div class="app-mark"></div>
    <div class="app-name">SUMMIT ROAMER</div>
    <p class="quote">“Traveling - it leaves you speechless, then turns you into a storyteller”</p>
    <p class="author">- Mira Castell</p>
    <div class="hop-btn">Let's Hop</div>
  </section>
</main>
</body>
</html>
```